Wordpress Design for Software Company

I have a website that is not developed in WordPress. I need the current site www.mirtawel.com/projects/plumvane to be redesigned in Wordpress. I would to keep some of the look and feel but change other things.
1) such as logo background color
2) have (3) columns in on inner pages
3) so nice pictures or graphic layouts I am hoping that you will be able to improve on the look of the website.
Target Market(s)
B2B Companies that deploy call centers or have inside sales staff.
Industry/Entity Type
It Company
Look and feel

```html
<!DOCTYPE html>
<html lang="en">
<head>
<meta charset="utf-8">
<title>Plumvane – Call Center Solutions</title>
<link rel="stylesheet" href="https://fonts.googleapis.com/css2?family=Ubuntu:ital,wght@0,300;0,400;0,500;1,300&display=swap">
<style>
:root{
  --sky:#2f8fd3;
  --sky-light:#cfe6f7;
  --navy:#13293a;
  --nav-text:#ffd23a;
  --orange:#f07a12;
  --orange-dark:#e04a10;
  --sidebar:#6fc0e6;
  --sidebar-top:#e9f5fb;
  --text:#4a4a4a;
  --muted:#555;
  --footer-bg:#dcdcdc;
}
*{margin:0;padding:0;box-sizing:border-box}
html,body{width:1200px;height:1051px;overflow:hidden}
body{
  font-family:"Ubuntu",sans-serif;color:var(--text);position:relative;
  background:
    radial-gradient(ellipse 180px 520px at 40px 420px,#5aa7dd 0%,rgba(90,167,221,0) 100%),
    radial-gradient(ellipse 180px 520px at 1160px 420px,#5aa7dd 0%,rgba(90,167,221,0) 100%),
    linear-gradient(#3e95d6 0,#bcdcf2 120px,#fff 260px,#fff 100%);
}
.page{position:absolute;left:133px;top:0;width:934px;height:977px;background:#fff;box-shadow:0 0 12px rgba(0,0,0,.12)}
.header{position:absolute;left:0;top:0;width:934px;height:90px;background:linear-gradient(#3a95d8,#d9ecf8 75%,#fff)}
.brand{position:absolute;left:24px;top:22px;display:flex;align-items:center;gap:8px;font-size:30px;color:#1f6fb3;font-weight:400}
.brand i{width:34px;height:34px;border-radius:50%;background:#1f6fb3;display:block}
.login{position:absolute;right:24px;top:8px;color:#fff;font-size:14px}
.search{position:absolute;left:661px;top:41px;width:254px;height:33px;background:#45a6dd;border-radius:3px}
.search span{position:absolute;left:14px;top:6px;width:190px;height:21px;background:#2c7fb1}
.search svg{position:absolute;right:10px;top:5px}
.nav{position:absolute;left:0;top:90px;width:934px;height:44px;background:var(--navy)}
.nav a{position:absolute;top:6px;height:33px;width:147px;border:1px solid #3a5566;background:linear-gradient(#24394a,#12222f);color:var(--nav-text);font-size:16px;text-align:center;line-height:31px;text-decoration:none}
.nav a.drop{padding-right:22px}
.nav a.drop::after{content:"";position:absolute;right:12px;top:13px;border:5px solid transparent;border-top:6px solid var(--orange)}
.social{position:absolute;right:18px;top:8px;display:flex;gap:6px}
.social i{width:28px;height:28px;border-radius:50%;display:block;background:#3d8fcf}
.social i:last-child{background:var(--orange)}
.banner{position:absolute;left:1px;top:136px;width:715px;height:285px;border-radius:6px;overflow:hidden;background:linear-gradient(90deg,#c7cdd3 0,#e6e2dc 45%,#f39a1a 58%,#f7c21a 85%,#f9d81a)}
.banner .photo{position:absolute;left:0;top:0;width:400px;height:285px;background:linear-gradient(90deg,#b9c0c8,#ddd6cf 70%,rgba(240,180,60,0))}
.banner h2{position:absolute;left:405px;top:22px;width:300px;text-align:center;color:#fff;font-weight:300;font-style:italic;font-size:27px;line-height:34px;white-space:nowrap}
.btn{position:absolute;left:492px;top:204px;width:164px;height:32px;background:linear-gradient(#ff6a2a,#e0360e);color:#fff;font-size:17px;line-height:32px;padding-left:18px}
.btn::after{content:"›";position:absolute;right:0;top:0;width:34px;text-align:center;font-size:26px;border-left:1px solid #ff9a6a;line-height:30px}
.dots{position:absolute;left:546px;top:252px;display:flex;gap:8px;align-items:center}
.dots i{width:12px;height:12px;border-radius:50%;background:#5b8fc7;display:block}
.dots i.on{background:var(--orange)}
.dots b{width:0;height:0;border:6px solid transparent;display:block}
.dots b.l{border-right:9px solid var(--orange-dark);border-left:0}
.dots b.r{border-left:9px solid var(--orange-dark);border-right:0}
.tabs{position:absolute;left:1px;top:435px;width:715px;height:304px;border:1px solid #ddd;border-radius:5px;background:linear-gradient(#e6e6e6,#fff 120px)}
.tabbar{position:absolute;left:4px;top:2px;right:4px;height:33px;border:1px solid #ccc;border-radius:4px;background:#e2e2e2}
.tab{position:absolute;top:4px;height:30px;padding:0 14px;border:1px solid #ccc;border-bottom:0;background:#f1f1f1;font-size:12px;line-height:30px;color:#555}
.tab.on{background:#fff}
.tabs h3{position:absolute;left:23px;top:50px;font-size:12px;font-weight:500;color:#444;display:flex;gap:6px;align-items:center}
.tabs h3 i{width:14px;height:10px;background:#777;display:block;border-radius:2px}
.tabs p{position:absolute;left:23px;font-size:12px;line-height:18.5px;color:var(--muted)}
.avatar{position:absolute;left:566px;top:87px;width:131px;height:131px;border:3px solid #fff;border-radius:6px;box-shadow:0 0 4px rgba(0,0,0,.3);background:linear-gradient(135deg,#b07a3a,#6b4a2a 50%,#2a2a2a)}
.side{position:absolute;left:726px;top:136px;width:208px;height:611px;background:linear-gradient(var(--sidebar-top),var(--sidebar))}
.side h4{position:absolute;left:0;width:208px;height:36px;background:linear-gradient(#2a3c4a,#132430);color:#fff;font-size:16px;font-weight:400;line-height:36px;padding-left:40px}
.side h4::before{content:"";position:absolute;left:11px;top:12px;width:20px;height:12px;border-radius:50%;background:#3d8fcf;box-shadow:8px 2px 0 -2px var(--orange)}
.side ul{position:absolute;left:14px;width:180px;list-style:none;font-size:11px;line-height:16px;color:#333}
.side li{padding-left:12px;position:relative;margin-bottom:11px}
.side li::before{content:"›";position:absolute;left:0;top:-1px;font-weight:700}
.more{position:absolute;left:108px;top:300px;color:#e58a10;font-size:11px}
.contact{position:absolute;left:21px;top:534px;width:177px;height:58px;background:#fff;border-radius:5px;font-size:11px;color:#222;padding:10px 0 0 8px;line-height:17px}
.contact small{color:var(--orange);font-size:9px}
.contact span{display:inline-block;width:14px;height:9px;background:var(--orange);margin-right:4px;vertical-align:-1px}
.footer{position:absolute;left:0;top:747px;width:934px;height:230px;background:linear-gradient(var(--footer-bg),#fff)}
.col{position:absolute;top:20px;width:220px;height:196px;font-size:13px;color:#333}
.col + .col{border-left:1px solid #ccc}
.col h5{font-size:16px;font-weight:400;color:#222;margin:0 0 10px 24px;position:relative}
.col h5::before{content:"";position:absolute;left:-8px;top:7px;width:4px;height:4px;background:var(--orange)}
.col ul{list-style:none;margin-left:24px;line-height:22.5px}
.copy{position:absolute;left:0;top:1008px;width:1200px;text-align:center;font-size:10px;color:var(--orange)}
</style>
</head>
<body>
<div class="page">
  <header class="header">
    <div class="brand"><i></i>Plumvane</div>
    <div class="login">Login</div>
    <div class="search"><span></span>
      <svg width="24" height="24" viewBox="0 0 24 24"><circle cx="10" cy="10" r="7" fill="none" stroke="#fff" stroke-width="2.5"/><path d="M15 15l6 6" stroke="#fff" stroke-width="3"/></svg>
    </div>
  </header>
  <nav class="nav">
    <a class="drop" style="left:4px">Products</a>
    <a style="left:157px">Solutions</a>
    <a style="left:310px">Resources</a>
    <a class="drop" style="left:463px">Services</a>
    <div class="social"><i></i><i></i><i></i></div>
  </nav>

  <section class="banner">
    <div class="photo" role="img" aria-label="Smiling call center agent wearing a headset in an office"></div>
    <h2>Lorem Ipsum is simply<br>dummy text of the<br>printing and<br>typesetting industry.<br>Lorem Ipsum has</h2>
    <div class="btn">Know More</div>
    <div class="dots"><b class="l"></b><i></i><i class="on"></i><i></i><b class="r"></b></div>
  </section>

  <section class="tabs">
    <div class="tabbar">
      <div class="tab on" style="left:2px">Who We Are</div>
      <div class="tab" style="left:105px">What We Do</div>
      <div class="tab" style="left:203px">Our Clients</div>
      <div class="tab" style="left:298px">Try Us Out</div>
    </div>
    <h3><i></i>About Plumvane Corporation</h3>
    <p style="top:82px">Practical <b>call center solutions</b> for the contact center industry</p>
    <p style="top:112px;width:530px">Plumvane is an industry-leader in the development of call center solutions and predictive dialers for industry-specific applications ranging from financial services to home remodeling and other related companies that utilize the services of Predictive Dialing and Contact Center Management &amp; Customer Interaction. We offer both premise based and hosted solutions to small to medium-sized inside sales organizations to larger call centers.</p>
    <p style="top:218px;width:670px">Our goal is to provide a seamless cost effective call center solutions which involves the cohesive blend of computer telephony integration (CTI) applications, web centric applications, customer relationship (CRM), agent interaction and other channels of communications such as web call back, web chat, email, fax and web collaboration</p>
    <div class="avatar" role="img" aria-label="Business professional in a suit with colleagues in the background"></div>
  </section>

  <aside class="side">
    <h4 style="top:0">What’s New</h4>
    <ul style="top:60px">
      <li>Remote IP Agent/Virtual Agent</li>
      <li>Plumvane and Veltrix Channel Network Partner Silverline Net Communication Provide a "Universal Phone" Solution to NY based Mortgage Finance Company</li>
      <li>Find out what people are saying about the Plumvane Hosted Predictive Dialer System</li>
      <li>More Press</li>
    </ul>
    <div class="more">Learn more &gt;&gt;</div>
    <h4 style="top:320px">Important Links</h4>
    <ul style="top:380px">
      <li>Products</li>
      <li>Hosted Applications</li>
      <li>Integrated Dialing Solutions</li>
      <li>Industry Specific Solutions</li>
    </ul>
    <div class="contact"><span></span>1.888.555.0142 <small>(Toll-free)</small><br><span></span>info@plumvanecorp.com</div>
  </aside>

  <footer class="footer">
    <div class="col" style="left:0"><h5>Products</h5><ul><li>Home</li><li>Products</li><li>Subpage</li><li>Resources</li><li>Sample Page</li><li>Services</li><li>Solutions</li></ul></div>
    <div class="col" style="left:224px"><h5>Solutions</h5><ul><li>Home</li><li>Products</li><li>Subpage</li><li>Resources</li><li>Sample Page</li><li>Services</li><li>Solutions</li></ul></div>
    <div class="col" style="left:448px"><h5>Resources</h5><ul><li>Home</li><li>Products</li><li>Subpage</li><li>Resources</li><li>Sample Page</li><li>Services</li><li>Solutions</li></ul></div>
    <div class="col" style="left:672px"><h5>Services</h5><ul><li>Home</li><li>Products</li><li>Subpage</li><li>Resources</li><li>Sample Page</li><li>Services</li><li>Solutions</li></ul></div>
  </footer>
</div>
<div class="copy">© 2011 plumvanecorp. All Rights Reserved.</div>
</body>
</html>
```